business card design

We are a company in Hong Kong, distribute & export aquariums and want a new business card. We have added our new fish tank in our new card but do want a better design.
Don't prefer fancy design as this is for export business and need to show overseas office contact.
But do want a professional design and a card that can tell we are in aquatic business.
I will attach a scan copy of current name card, the revised draft we just make, the content to show on name card and the logos
feel free to visit our webpage www.qv-reefhouse.com for more details.

```html
<!DOCTYPE html>
<html lang="en">
<head>
<meta charset="utf-8">
<title>Business Card – Marcus Lee</title>
<link rel="stylesheet" href="https://fonts.googleapis.com/css2?family=Roboto:ital,wght@0,300;0,400;0,500;0,700;1,400&family=Noto+Sans+TC:wght@400;500&display=swap">
<style>
  :root {
    --page: #e9e9e7;
    --card: #ffffff;
    --ink: #1e1e1e;
    --muted: #555555;
    --navy: #1f3f8f;
    --red: #d8222a;
    --rule: #333333;
    --pale: #eeeeee;
  }
  * { box-sizing: border-box; margin: 0; padding: 0; }
  html, body { width: 1200px; height: 900px; overflow: hidden; }
  body {
    background: var(--page);
    font-family: "Roboto", "Noto Sans TC", sans-serif;
    color: var(--ink);
    position: relative;
  }
  .card {
    position: absolute;
    left: 250px;
    width: 700px;
    height: 420px;
    background: var(--card);
    overflow: hidden;
    box-shadow: 0 2px 10px rgba(0,0,0,.12);
  }
  .card--back { top: 20px; }
  .card--front { top: 460px; }

  /* ---------- back ---------- */
  .tank-photo {
    position: absolute; left: 0; top: 0; width: 330px; height: 420px;
    background: radial-gradient(ellipse at 75% 45%, #ffffff 0%, #eef1f3 45%, #c9ced3 80%, #3a3d42 100%);
  }
  .tank-rim {
    position: absolute; right: 0; top: 0; width: 700px; height: 420px; pointer-events: none;
  }
  .offices {
    position: absolute; left: 350px; top: 40px; width: 300px;
  }
  .office { margin-bottom: 30px; }
  .office__name {
    font-weight: 700; font-size: 15px; color: var(--navy); margin-bottom: 8px;
  }
  .office__name--zh { font-family: "Noto Sans TC", sans-serif; font-weight: 500; font-size: 13px; margin-bottom: 2px; }
  .office__row { display: flex; gap: 18px; font-size: 10px; color: var(--navy); line-height: 1.5; }
  .office__col { display: flex; gap: 6px; }
  .office__col--phone { width: 120px; flex: none; }
  .icon { width: 10px; height: 10px; flex: none; margin-top: 2px; fill: var(--navy); }

  /* ---------- front ---------- */
  .edge-mark {
    position: absolute; left: 0; top: 125px; width: 30px; height: 80px; background: var(--ink);
  }
  .person { position: absolute; left: 60px; top: 135px; }
  .person__name { font-weight: 300; font-size: 34px; letter-spacing: .5px; }
  .person__name .zh { font-family: "Noto Sans TC", sans-serif; font-weight: 400; }
  .person__title { font-style: italic; font-size: 11px; color: var(--muted); margin: 6px 0 0 40px; }
  .company {
    position: absolute; left: 60px; top: 232px; font-size: 14px;
  }
  .company .zh { font-family: "Noto Sans TC", sans-serif; margin-left: 6px; }
  .brands { position: absolute; left: 60px; top: 268px; display: flex; align-items: center; gap: 22px; }
  .badge-seal { width: 58px; height: 58px; border-radius: 50%; background: var(--navy); margin-top: 40px; }
  .brand { font-weight: 700; font-size: 14px; color: var(--navy); display: flex; align-items: center; gap: 6px; white-space: nowrap; }
  .brand__square { width: 14px; height: 14px; background: var(--navy); }
  .brand--group { color: var(--ink); font-size: 13px; }
  .brand--group .brand__square { background: var(--red); }
  .tank-round {
    position: absolute; left: 505px; top: 20px; width: 120px; height: 120px; border-radius: 50%;
    background: radial-gradient(circle at 50% 50%, #f4f6f7 0%, #dfe3e6 52%, #2a2c30 58%, #1a1b1e 100%);
  }
  .divider { position: absolute; left: 430px; top: 150px; width: 1px; height: 175px; background: var(--rule); }
  .contacts { position: absolute; left: 447px; top: 150px; font-size: 11px; line-height: 1.5; list-style: none; }
  .contact { display: flex; gap: 10px; margin-bottom: 4px; }
  .contact .icon { fill: var(--ink); margin-top: 3px; }
  .contact .zh { font-family: "Noto Sans TC", sans-serif; font-weight: 500; }
  .band { position: absolute; left: 0; top: 0; width: 700px; height: 420px; }
</style>
</head>
<body>

<section class="card card--back" aria-label="Card back: overseas offices">
  <div class="tank-photo" role="img" aria-label="Photo inside a round aquarium with goldfish, rising bubbles and red water plants"></div>
  <svg class="tank-rim" viewBox="0 0 700 420" aria-hidden="true">
    <path d="M560 0 Q700 60 700 200 L700 0 Z" fill="#5b6066"/>
  </svg>

  <div class="offices">
    <article class="office">
      <h2 class="office__name">QV Reefhouse GmbH</h2>
      <div class="office__row">
        <div class="office__col office__col--phone">
          <svg class="icon" viewBox="0 0 10 10"><path d="M2 0h2l1 2.5-1.3 1a5 5 0 0 0 2.8 2.8l1-1.3L10 6v2a2 2 0 0 1-2 2A8 8 0 0 1 0 2a2 2 0 0 1 2-2z"/></svg>
          <span>+49 30 5550 1234<br>+49 30 5550 1235</span>
        </div>
        <div class="office__col">
          <svg class="icon" viewBox="0 0 10 10"><path d="M5 0a3.5 3.5 0 0 1 3.5 3.5C8.5 6 5 10 5 10S1.5 6 1.5 3.5A3.5 3.5 0 0 1 5 0zm0 2a1.5 1.5 0 1 0 0 3 1.5 1.5 0 0 0 0-3z"/></svg>
          <span>Uferweg 21,<br>10115 Berlin, Germany</span>
        </div>
      </div>
    </article>

    <article class="office">
      <h2 class="office__name">QV Reefhouse Inc.</h2>
      <div class="office__row">
        <div class="office__col office__col--phone">
          <svg class="icon" viewBox="0 0 10 10"><path d="M2 0h2l1 2.5-1.3 1a5 5 0 0 0 2.8 2.8l1-1.3L10 6v2a2 2 0 0 1-2 2A8 8 0 0 1 0 2a2 2 0 0 1 2-2z"/></svg>
          <span>+1 555 014 7321<br>+1 555 014 7322</span>
        </div>
        <div class="office__col">
          <svg class="icon" viewBox="0 0 10 10"><path d="M5 0a3.5 3.5 0 0 1 3.5 3.5C8.5 6 5 10 5 10S1.5 6 1.5 3.5A3.5 3.5 0 0 1 5 0zm0 2a1.5 1.5 0 1 0 0 3 1.5 1.5 0 0 0 0-3z"/></svg>
          <span>PO Box 412, Maple Bay,<br>OR 97000, United States</span>
        </div>
      </div>
    </article>

    <article class="office">
      <h2 class="office__name office__name--zh">東莞市海線電器有限公司</h2>
      <h2 class="office__name">Dongguan Harbourline Appliance Company Limited</h2>
      <div class="office__row">
        <div class="office__col office__col--phone">
          <svg class="icon" viewBox="0 0 10 10"><path d="M2 0h2l1 2.5-1.3 1a5 5 0 0 0 2.8 2.8l1-1.3L10 6v2a2 2 0 0 1-2 2A8 8 0 0 1 0 2a2 2 0 0 1 2-2z"/></svg>
          <span>+86 769 5550 2140<br>+86 769 5550 2141</span>
        </div>
        <div class="office__col">
          <svg class="icon" viewBox="0 0 10 10"><path d="M5 0a3.5 3.5 0 0 1 3.5 3.5C8.5 6 5 10 5 10S1.5 6 1.5 3.5A3.5 3.5 0 0 1 5 0zm0 2a1.5 1.5 0 1 0 0 3 1.5 1.5 0 0 0 0-3z"/></svg>
          <span>Riverside Industrial Park,<br>Dongguan, Guangdong, China 523900</span>
        </div>
      </div>
    </article>
  </div>
</section>

<section class="card card--front" aria-label="Card front: Marcus Lee">
  <svg class="band" viewBox="0 0 700 420" aria-hidden="true">
    <polygon points="300,420 700,330 700,420" fill="var(--pale)"/>
    <polygon points="300,420 700,330 700,352 395,420" fill="var(--red)"/>
  </svg>

  <div class="tank-round" role="img" aria-label="Round wall-mounted fish tank with small fish and plants"></div>

  <div class="edge-mark"></div>
  <div class="person">
    <h1 class="person__name">Marcus Lee - <span class="zh">李文浩</span></h1>
    <p class="person__title">Marketing &amp; Sales Manager – Aquarium</p>
  </div>

  <p class="company">Tidewell Holdings Co., Ltd. <span class="zh">潮匯集團有限公司</span></p>

  <div class="brands">
    <div class="badge-seal" aria-hidden="true"></div>
    <div class="brand"><span class="brand__square"></span>QV Reefhouse</div>
    <div class="brand brand--group"><span class="brand__square"></span>TIDEWELL GROUP</div>
  </div>

  <div class="divider"></div>
  <ul class="contacts">
    <li class="contact">
      <svg class="icon" viewBox="0 0 10 10"><path d="M2 0h2l1 2.5-1.3 1a5 5 0 0 0 2.8 2.8l1-1.3L10 6v2a2 2 0 0 1-2 2A8 8 0 0 1 0 2a2 2 0 0 1 2-2z"/></svg>
      <span>Tel: (852) 2555 0148<br>Fax: (852) 2555 0192</span>
    </li>
    <li class="contact">
      <svg class="icon" viewBox="0 0 10 10"><path d="M0 2h10v6H0z M0 2l5 3.5L10 2" fill="none" stroke="currentColor" stroke-width="1"/></svg>
      <span>marcus_lee@qv-reefhouse.com<br>www.qv-reefhouse.com</span>
    </li>
    <li class="contact">
      <svg class="icon" viewBox="0 0 10 10"><path d="M5 0a3.5 3.5 0 0 1 3.5 3.5C8.5 6 5 10 5 10S1.5 6 1.5 3.5A3.5 3.5 0 0 1 5 0zm0 2a1.5 1.5 0 1 0 0 3 1.5 1.5 0 0 0 0-3z"/></svg>
      <span>8/F., 17 Harbour View Road,<br>Kwun Tong, Kowloon, Hong Kong<br><span class="zh">香港九龍觀塘海景道十七號八樓</span></span>
    </li>
  </ul>
</section>

</body>
</html>
```